Wirenexa

I'm looking to much improve our current website wirenexa.com
Updates

Low design quality

Target Market(s)

Commercial clients (Not-Residentials)

Industry/Entity Type

Office buildings and Industrial clients

Coding

Coded - Design and coding required

Number of Pages Required

5+ page

Requirements
Must have
• Very professional structured low voltage cabling projects for Wi-Fi, Audio/Video conference rooms, Access Control systems, CCTV.

```html
<!DOCTYPE html>
<html lang="en">
<head>
<meta charset="utf-8">
<title>Wirenexa — Commercial Technology Infrastructure</title>
<link href="https://fonts.googleapis.com/css2?family=Inter+Tight:wght@600;700&family=Inter:wght@400;500&family=JetBrains+Mono:wght@400;500&display=swap" rel="stylesheet">
<style>
:root{
  --bg:#111112;
  --panel:#161617;
  --card:#151516;
  --line:#2c2d2f;
  --line-soft:#3a3b3e;
  --red:#d92b2b;
  --text:#ecebea;
  --muted:#bdbcbb;
  --dim:#8b8a89;
  --grey-bar:#6e7274;
}
*{box-sizing:border-box;margin:0;padding:0}
html,body{width:714px;height:1200px;overflow:hidden;background:var(--bg)}
body{position:relative;font-family:"Inter",sans-serif;color:var(--text)}
.abs{position:absolute}
.mono{font-family:"JetBrains Mono",monospace;letter-spacing:.12em;text-transform:uppercase}
.head{font-family:"Inter Tight",sans-serif;font-weight:700;letter-spacing:-.02em;text-transform:uppercase}
.red{color:var(--red)}

/* header */
.site-header{left:0;top:0;width:714px;height:45px;border-bottom:1px solid var(--line);background:var(--bg)}
.brand{display:flex;align-items:center;gap:5px;font-family:"Inter Tight",sans-serif;font-weight:700;color:var(--text)}
.brand-mark{width:12px;height:12px;background:var(--red)}
.site-header .brand{left:19px;top:11px;font-size:22px}
.nav{left:284px;top:17px;display:flex;gap:18px;font-size:6.6px}
.nav a{color:var(--text);text-decoration:none}
.nav a.active{color:var(--red);border-bottom:1px solid var(--red);padding-bottom:2px}
.cta{left:565px;top:12px;width:131px;height:20px;background:var(--red);color:#fff;font-size:6.6px;display:flex;align-items:center;justify-content:center;gap:4px}

/* hero */
.hero{left:0;top:45px;width:714px;height:513px;border-bottom:1px solid var(--line);
  background:radial-gradient(ellipse at 50% 50%,#3a3a3b 0%,#262627 45%,#18181a 100%)}
.status{left:18px;top:216px;height:12px;padding:0 7px;border:1px solid #6a6a6a;font-size:6.6px;color:var(--red);display:flex;align-items:center;gap:5px;background:rgba(17,17,18,.6)}
.dot{width:4px;height:4px;border-radius:50%;background:var(--red);display:inline-block}
.hero-title{left:18px;top:244px;font-size:26px;line-height:30px}
.hero-copy{left:18px;top:314px;width:400px;font-size:8.7px;line-height:14.5px;color:var(--text)}
.btn{top:361px;height:25px;font-size:6.6px;display:flex;align-items:center;justify-content:center;gap:5px}
.btn-primary{left:18px;width:114px;background:var(--red);color:#fff}
.btn-ghost{left:141px;width:96px;border:1px solid #5a5a5a;color:var(--red)}

.diag{left:479px;top:239px;width:217px;height:124px;background:rgba(17,17,18,.92);padding:12px 13px}
.diag-head{display:flex;justify-content:space-between;font-size:6.6px;padding-bottom:5px;border-bottom:1px solid var(--line-soft)}
.metric{margin-top:13px;font-family:"JetBrains Mono",monospace;font-size:7.2px;display:flex;justify-content:space-between}
.bar{margin-top:8px;height:2px;background:#2f3032;position:relative}
.bar span{position:absolute;left:0;top:0;height:2px}

/* systems */
.sec-title{left:18px;top:612px;display:flex;align-items:center;gap:10px;font-size:17px}
.sec-sub{left:18px;top:643px;font-size:7.8px;color:var(--text)}
.card{background:var(--card);padding:12px 13px;border-radius:3px}
.card .tag{font-size:6.6px;color:var(--text)}
.card .icon{position:absolute;right:13px;top:10px}
.card h3{font-family:"Inter Tight",sans-serif;font-weight:600;text-transform:uppercase;font-size:10.8px;letter-spacing:-.01em}
.card p{font-size:7.6px;line-height:11.8px;color:var(--muted)}
.card .rule{position:absolute;left:13px;right:13px;height:1px;background:var(--line-soft)}
.spec{font-family:"JetBrains Mono",monospace;font-size:7.2px}
.spec small{display:block;font-size:6.3px;letter-spacing:.12em;color:var(--dim);margin-bottom:1px}
.foot-tag{position:absolute;left:13px;font-family:"JetBrains Mono",monospace;font-size:7.2px;color:var(--red)}

/* footer */
.footer-top{left:0;top:1037px;width:714px;height:1px;background:#34383a}
.footer .brand{left:18px;top:1072px;font-size:18px}
.footer-tagline{left:18px;top:1104px;font-size:6.6px;letter-spacing:.06em}
.fcol{top:1072px}
.fcol h4{font-family:"JetBrains Mono",monospace;font-weight:400;font-size:6.6px;letter-spacing:.14em;color:var(--dim);margin-bottom:11px}
.fcol a{display:block;font-size:7.8px;color:var(--text);text-decoration:none;margin-bottom:8.5px}
.footer-bottom{left:0;top:1175px;width:714px;height:25px;border-top:1px solid var(--line);background:#0e0e0f}
.copy{left:18px;top:8px;font-size:6.8px;letter-spacing:.06em}
.online{right:18px;top:8px;font-size:6.8px;color:var(--red);display:flex;align-items:center;gap:5px;letter-spacing:.04em}
</style>
</head>
<body>

<header class="abs site-header">
  <div class="abs brand"><span class="brand-mark"></span>Wirenexa</div>
  <nav class="abs nav mono"><a class="active" href="#">Services</a><a href="#">Projects</a><a href="#">Process</a></nav>
  <a class="abs cta mono">Request Consultation
    <svg width="7" height="7" viewBox="0 0 10 10"><path d="M1 5h8M5.5 1.5 9 5l-3.5 3.5" stroke="#fff" stroke-width="1.4" fill="none"/></svg></a>
</header>

<section class="abs hero" role="img" aria-label="Dark photo of an empty commercial building interior with exposed ceiling and columns"></section>

<div class="abs status mono"><span class="dot"></span>System Status: Nominal</div>
<h1 class="abs hero-title head">Commercial Technology<br><span class="red">Infrastructure</span></h1>
<p class="abs hero-copy">Structured cabling, enterprise Wi-Fi, AV systems, access control, and security infrastructure engineered for mission-critical commercial and industrial environments.</p>
<a class="abs btn btn-primary mono">Deploy Systems
  <svg width="9" height="7" viewBox="0 0 12 10"><rect x=".6" y=".6" width="10.8" height="8.8" fill="none" stroke="#fff" stroke-width="1.1"/><path d="M3 3l2 2-2 2M6 7h3" stroke="#fff" stroke-width="1.1" fill="none"/></svg></a>
<a class="abs btn btn-ghost mono">View Specs <span>{}</span></a>

<aside class="abs diag">
  <div class="diag-head mono"><span>Network Diagnostics</span>
    <svg width="8" height="7" viewBox="0 0 10 8"><path d="M1 7V5M3.5 7V3.5M6 7V4.5M8.5 7V2M1 3l3-2 2 2 3-2" stroke="#d92b2b" stroke-width="1" fill="none"/></svg></div>
  <div class="metric"><span>Uplink Speed</span><span class="red">9.8 Gbps</span></div>
  <div class="bar"><span style="width:98%;background:var(--red)"></span></div>
  <div class="metric"><span>Active Nodes</span><span>1,248</span></div>
  <div class="bar"><span style="width:75%;background:var(--grey-bar)"></span></div>
  <div class="metric"><span>Latency</span><span>1.2ms</span></div>
  <div class="bar"><span style="width:10%;background:var(--grey-bar)"></span></div>
</aside>

<h2 class="abs sec-title head">
  <svg width="11" height="11" viewBox="0 0 12 12"><rect x=".7" y=".7" width="10.6" height="4.5" fill="none" stroke="#d92b2b" stroke-width="1.2"/><rect x=".7" y="6.8" width="10.6" height="4.5" fill="none" stroke="#d92b2b" stroke-width="1.2"/></svg>
  Core Systems Architecture</h2>
<p class="abs sec-sub">Modular, high-density infrastructure solutions designed for rapid deployment and sustained reliability.</p>

<article class="abs card" style="left:18px;top:690px;width:449px;height:148px">
  <div class="tag mono">Module 01</div>
  <svg class="icon" width="14" height="11" viewBox="0 0 14 11"><path d="M1 4a8.5 8.5 0 0 1 12 0M3 6.3a5.5 5.5 0 0 1 8 0M5 8.5a2.6 2.6 0 0 1 4 0" stroke="#d92b2b" stroke-width="1.4" fill="none"/><circle cx="7" cy="10" r=".9" fill="#d92b2b"/></svg>
  <h3 style="margin-top:24px">Enterprise Wi-Fi</h3>
  <p style="margin-top:5px;width:245px">High-density wireless access point deployment utilizing Wi-Fi 6E architecture. Heatmap-driven design ensures absolute coverage in complex environments.</p>
  <div class="rule" style="top:109px"></div>
  <div class="abs spec" style="left:13px;top:118px"><small>STANDARD</small><span class="red">802.11ax (6E)</span></div>
  <div class="abs spec" style="left:229px;top:118px"><small>TOPOLOGY</small>Mesh / Controller</div>
</article>

<article class="abs card" style="left:476px;top:690px;width:220px;height:151px">
  <div class="tag mono">Module 02</div>
  <svg class="icon" width="11" height="12" viewBox="0 0 11 12"><path d="M2.5 11V4a2 2 0 0 1 4 0v4a2 2 0 0 0 4 0V1" stroke="#d92b2b" stroke-width="1.3" fill="none"/><circle cx="2.5" cy="10" r="1.4" fill="#d92b2b"/><circle cx="9" cy="1.6" r="1.4" fill="#d92b2b"/></svg>
  <h3 style="margin-top:30px">Structured Cabling</h3>
  <p style="margin-top:5px">Cat6A and Fiber Optic backbone installations.</p>
  <div class="rule" style="top:112px"></div>
  <div class="abs spec" style="left:13px;top:119px;line-height:12px"><span class="dot" style="width:3px;height:3px;margin-right:5px;vertical-align:middle"></span>Cat6 / Cat6A Copper<br><span class="dot" style="width:3px;height:3px;margin-right:5px;vertical-align:middle"></span>Single/Multi-mode Fiber</div>
</article>

<article class="abs card" style="left:18px;top:851px;width:220px;height:131px">
  <div class="tag mono">Module 03</div>
  <svg class="icon" width="10" height="11" viewBox="0 0 10 11"><path d="M1 10.5V.7h6v9.8M7 2.5h2v8M.2 10.5h9.6M4.3 5.5v1" stroke="#d92b2b" stroke-width="1.2" fill="none"/></svg>
  <h3 style="margin-top:34px">AV Conference Rooms</h3>
  <p style="margin-top:5px">Integrated video conferencing and presentation systems.</p>
  <div class="rule" style="top:103px"></div>
  <div class="foot-tag" style="top:114px">Meetline / Roomcast Cert.</div>
</article>

<article class="abs card" style="left:247px;top:851px;width:220px;height:131px">
  <div class="tag mono">Module 04</div>
  <svg class="icon" width="10" height="12" viewBox="0 0 10 12"><rect x=".8" y="5" width="8.4" height="6.3" fill="none" stroke="#d92b2b" stroke-width="1.2"/><path d="M2.7 5V3.3a2.3 2.3 0 0 1 4.6 0V5" stroke="#d92b2b" stroke-width="1.2" fill="none"/><path d="M5 7.4v1.6" stroke="#d92b2b" stroke-width="1.2"/></svg>
  <h3 style="margin-top:34px">Access Control</h3>
  <p style="margin-top:5px">Biometric and card-based IP security gateways.</p>
  <div class="rule" style="top:103px"></div>
  <div class="foot-tag" style="top:114px">Cloud-Managed Relays</div>
</article>

<article class="abs card" style="left:476px;top:851px;width:220px;height:131px">
  <div class="tag mono">Module 05</div>
  <svg class="icon" width="12" height="9" viewBox="0 0 12 9"><rect x=".7" y=".7" width="7.6" height="7.6" fill="none" stroke="#d92b2b" stroke-width="1.2"/><path d="M8.3 3.5 11.3 1.5v6l-3-2" fill="#d92b2b"/></svg>
  <h3 style="margin-top:34px">CCTV Systems</h3>
  <p style="margin-top:5px">High-definition IP surveillance with AI analytics.</p>
  <div class="rule" style="top:103px"></div>
  <div class="foot-tag" style="top:114px">PoE+ NVR Architectures</div>
</article>

<footer class="footer">
  <div class="abs footer-top"></div>
  <div class="abs brand"><span class="brand-mark" style="width:10px;height:10px"></span>Wirenexa</div>
  <div class="abs footer-tagline mono">Engineered Infrastructure Solutions</div>
  <div class="abs fcol" style="left:190px"><h4>SYSTEMS</h4><a>Structured Cabling</a><a>Enterprise Wi-Fi</a><a>AV Systems</a></div>
  <div class="abs fcol" style="left:361px"><h4>SECURITY</h4><a>Access Control</a><a>CCTV</a></div>
  <div class="abs fcol" style="left:533px"><h4>COMPANY</h4><a>Consultation</a><a>Case Studies</a><a>Privacy Policy</a></div>
  <div class="abs footer-bottom">
    <div class="abs copy mono">© 2026 Wirenexa. All rights reserved. ISO 27001 certified.</div>
    <div class="abs online mono"><span class="dot"></span>SYS_ONLINE</div>
  </div>
</footer>

</body>
</html>
```